Website for Youth Orchestra to sell tickets and attract young musicians

We are looking for a new website design for a Youth Orchestra; one of the best classical youth orchestras in the county. This project is the design only. <br/><br/>The website serves two main purposes:<br/>• Selling tickets for concerts and performances of the orchestra<br/>• Recruiting young musicians to do audition for the orchestra<br/>
Updates

Target Market(s)

Classical music lovers with a special interest in young upcoming musicians.
Young talented musicians

Number of Pages Required

2 page

Colors
ec1f27

Requirements
Must have
• - A Picture on the front page that promotes the main upcomming event
• - Attention for recruiting new musicians
• - Pictures with young musicians (white back ground, see examples)
• - Responsive
• - Please use the logo attached
Should not have
• The brown colors of the current website (kvb-veldhorst.example)

```html
<!DOCTYPE html>
<html lang="en">
<head>
<meta charset="utf-8">
<title>Eemstad Jeugd Orkest</title>
<link rel="stylesheet" href="https://fonts.googleapis.com/css2?family=Rubik:wght@400;500;700&family=Roboto:wght@400;500;700&display=swap">
<style>
:root{
  --red:#ec1f27;
  --red-deep:#d8171f;
  --ink:#222222;
  --text:#444444;
  --muted:#666666;
  --light:#f1f1f1;
  --grey:#ebebeb;
  --black:#0b0b0b;
  --white:#ffffff;
}
*{box-sizing:border-box;margin:0;padding:0}
html,body{width:1200px;height:3812px;overflow:hidden}
body{font-family:"Roboto",Arial,sans-serif;color:var(--text);background:var(--white);position:relative}
.section{position:absolute;left:0;width:1200px;overflow:hidden}
.abs{position:absolute}
.btn{display:inline-flex;align-items:center;justify-content:center;background:var(--red);color:var(--white);font-family:"Rubik",Arial,sans-serif;font-weight:500;text-transform:uppercase;text-decoration:none;letter-spacing:.3px}
.brand{font-family:"Rubik",Arial,sans-serif;font-weight:700;color:var(--white);text-align:center;line-height:1.02;text-transform:lowercase}

/* header */
.site-header{top:0;height:155px;background:#f2f2f0;border-top:5px solid var(--red)}
.subscribe{left:127px;top:33px;width:289px;height:42px;background:var(--white);border:1px solid #cfcfcf;display:flex;align-items:center;padding:0 4px 0 16px}
.subscribe span{flex:1;font-size:11px;font-weight:500;color:#555;display:flex;align-items:center;gap:8px}
.subscribe .btn{height:30px;width:92px;font-size:11px}
.logo-cap{left:492px;top:-5px;width:216px;height:112px;background:var(--red);border-radius:0 0 108px 108px;display:flex;align-items:center;justify-content:center}
.logo-cap .brand{font-size:25px;margin-top:-6px}
.follow{right:118px;top:42px;display:flex;align-items:center;gap:8px;font-size:14px;font-weight:500;color:var(--ink)}
.follow i{width:25px;height:25px;border-radius:50%;display:block}
.main-nav{left:129px;top:121px;display:flex;gap:17px;font-size:13.5px;font-weight:500;color:var(--ink);text-transform:uppercase}
.main-nav a{color:inherit;text-decoration:none;display:flex;align-items:center;gap:6px}
.main-nav a.active{color:var(--red)}
.main-nav svg{width:9px;height:6px}

/* hero */
.hero{top:155px;height:474px;background:linear-gradient(90deg,#f2ede5 0%,#efe7dc 55%,#e9dfd2 100%)}
.hero-photo{left:520px;top:0;width:680px;height:474px;background:radial-gradient(ellipse at 60% 45%,#d8a47e 0%,#c98e6a 18%,#e6d3c2 45%,rgba(236,227,215,0) 70%)}
.hero-title{left:129px;top:60px;width:440px;font-family:"Rubik",Arial,sans-serif;font-weight:700;font-size:29px;line-height:34px;color:var(--ink);text-transform:uppercase}
.hero .btn{left:132px;top:249px;width:127px;height:47px;font-size:18px}
.slider-arrows{left:134px;top:343px;display:flex;gap:10px}
.slider-arrows span{width:31px;height:31px;background:#1c1c1c;display:flex;align-items:center;justify-content:center}

/* concerts */
.concerts{top:629px;height:540px;background:var(--light)}
.cap{background:var(--red);display:flex;align-items:center;justify-content:center;color:var(--white);font-family:"Rubik",Arial,sans-serif;font-weight:700;text-transform:uppercase}
.concerts .cap{left:444px;top:0;width:312px;height:102px;border-radius:0 0 156px 156px/0 0 102px 102px;font-size:25px;padding-bottom:18px}
.card{top:133px;width:222px;height:358px;background:var(--white);box-shadow:0 2px 10px rgba(0,0,0,.12);padding:10px}
.card .thumb{height:123px;background:linear-gradient(160deg,#4a3a2a,#1c1613 70%)}
.card h3{font-family:"Roboto",Arial,sans-serif;font-size:13.5px;font-weight:700;color:var(--ink);margin:19px 7px 6px}
.card p{font-size:11.5px;line-height:16px;color:var(--muted);margin:0 7px}
.card .when{position:absolute;left:17px;right:17px;top:228px;border-top:1px solid #cfcfcf;border-bottom:1px solid #cfcfcf;padding:9px 0 10px;font-size:12.5px;font-weight:500;color:var(--ink);line-height:17px;text-transform:uppercase}
.card .btn{position:absolute;left:17px;right:17px;top:296px;height:36px;font-size:15px}
.round-arrow{top:295px;width:38px;height:38px;border-radius:50%;border:1.5px solid #9a9a9a;display:flex;align-items:center;justify-content:center}

/* welcome */
.welcome{top:1169px;height:514px;background:#e8ddcf}
.welcome-photo{left:0;top:0;width:650px;height:514px;background:radial-gradient(ellipse at 38% 55%,#8a6a4f 0%,#b89677 30%,#dccab5 62%,#e8ddcf 80%)}
.welcome-text{left:661px;top:52px;width:405px}
.welcome-text h2{font-family:"Rubik",Arial,sans-serif;font-weight:500;font-size:25px;color:var(--ink);line-height:32px}
.welcome-text h2 strong{display:block;color:var(--red);font-weight:700;font-size:29px;line-height:38px}
.rule{width:52px;height:3px;background:#9c958d;margin:14px 0 36px}
.welcome-text p{font-size:15.5px;line-height:22.5px;color:#333}
.welcome-text .btn{margin-top:34px;width:112px;height:38px;font-size:14px}

/* ticket sale */
.ticket-sale{top:1683px;height:389px;background:linear-gradient(90deg,#e21c26,#ec1f27 45%,#e11922)}
.ticket-copy{left:139px;top:60px;width:380px;color:var(--white)}
.ticket-copy h2{font-family:"Rubik",Arial,sans-serif;font-weight:700;font-size:25px;line-height:32px;text-transform:uppercase}
.ticket-copy p{font-size:10.5px;line-height:21px;margin-top:22px;opacity:.95}
.ghost-btn{margin-top:24px;display:inline-flex;align-items:center;justify-content:center;width:117px;height:37px;border:2px solid var(--white);border-radius:20px;color:var(--white);font-family:"Rubik",Arial,sans-serif;font-weight:500;font-size:11px;text-transform:uppercase}
.poster{left:582px;top:29px;width:479px;height:333px;background:linear-gradient(165deg,#e7d7f0 0%,#dccbea 50%,#f0633a 62%,#ee4b2a 100%)}

/* upcoming */
.upcoming{top:2072px;height:592px;background:var(--grey)}
.band-photo{left:0;top:0;width:534px;height:592px;background:radial-gradient(ellipse at 50% 40%,#8b3a4f 0%,#4a1b2a 45%,#160a10 100%)}
.upcoming h2{left:588px;top:53px;font-family:"Rubik",Arial,sans-serif;font-weight:700;font-size:25px;color:var(--ink);text-transform:uppercase}
.upcoming h2 span{color:var(--red)}
.event{left:588px;width:520px;display:flex;gap:15px}
.date{width:63px;height:88px;background:#1b1b1b;color:var(--white);text-align:center;font-family:"Rubik",Arial,sans-serif;font-weight:500;flex:none;padding-top:9px}
.date small{display:block;font-size:13px;line-height:14px}
.date b{display:block;font-size:31px;line-height:34px;font-weight:700}
.date em{display:block;font-style:normal;font-size:12px}
.event h3{font-family:"Rubik",Arial,sans-serif;font-weight:500;font-size:16px;color:var(--red);text-transform:uppercase;margin-top:-4px}
.event p{font-size:14.5px;line-height:21.5px;color:#444;margin-top:4px}
.event p b{color:var(--ink);font-size:13px}
.upcoming .btn{left:588px;top:513px;width:112px;height:35px;font-size:14px}

/* recruiting */
.recruiting{top:2664px;height:479px;background:var(--black)}
.recruit-photo{left:480px;top:0;width:720px;height:479px;background:radial-gradient(ellipse at 55% 40%,#b88766 0%,#5a3a2a 28%,#1a1210 55%,#050505 80%)}
.recruit-panel{left:0;top:0;width:600px;height:479px;background:linear-gradient(90deg,var(--red) 0%,var(--red) 62%,rgba(236,31,39,0) 100%)}
.recruit-copy{left:129px;top:48px;color:var(--white)}
.recruit-copy h2{font-family:"Rubik",Arial,sans-serif;font-weight:700;font-size:31px;line-height:38px}
.recruit-copy .lead{font-size:18.5px;margin-top:2px}
.recruit-copy .rule{background:var(--white);margin:22px 0 28px}
.recruit-copy ul{list-style:none;font-size:22px;line-height:44px;font-weight:400}
.recruit-copy .apply{margin-top:22px;display:inline-flex;align-items:center;justify-content:center;width:116px;height:37px;background:var(--white);color:var(--red);font-family:"Rubik",Arial,sans-serif;font-weight:700;font-size:14px;text-transform:uppercase}

/* partners */
.partners{top:3143px;height:265px;background:var(--light)}
.partners .cap{left:440px;top:0;width:320px;height:110px;border-radius:0 0 160px 160px/0 0 110px 110px;font-size:25px;padding-bottom:10px}
.partner-row{left:128px;top:162px;width:944px;height:60px;display:flex;align-items:center;justify-content:space-between}
.partner{font-family:"Roboto",Arial,sans-serif;font-weight:500;font-size:17px;color:#2a3a7a;display:flex;align-items:center;gap:8px}
.partner i{width:14px;height:14px;display:block;background:var(--red)}
.partner.boxed{border:2px solid #333;padding:6px 12px;font-size:13px;letter-spacing:2px;color:#333}
.chev{top:182px}

/* footer */
.site-footer{top:3408px;height:404px;background:var(--black)}
.footer-photo{left:0;top:0;width:570px;height:404px;background:radial-gradient(ellipse at 45% 45%,#a9705a 0%,#4a2a22 30%,#120c0b 60%,#0b0b0b 85%)}
.site-footer .logo-cap{left:541px;top:0;width:216px;height:104px}
.footer-links{top:156px;font-size:12.5px;line-height:24px;color:#bbbbbb;text-transform:uppercase;list-style:none}
.footer-line{left:579px;top:282px;width:491px;height:1px;background:#444}
.footer-follow{left:579px;top:336px;display:flex;align-items:center;gap:8px;font-size:13px;color:#cccccc;font-weight:500}
.footer-follow i{width:24px;height:24px;border-radius:50%;display:block}
.copyright{left:870px;top:340px;font-size:11px;color:#cccccc}
</style>
</head>
<body>

<header class="section site-header">
  <form class="abs subscribe">
    <span><svg width="11" height="9" viewBox="0 0 11 9"><rect x=".5" y=".5" width="10" height="8" fill="none" stroke="#555"/><path d="M.5 .5 5.5 5 10.5 .5" fill="none" stroke="#555"/></svg>E MAIL ID</span>
    <span class="btn">Subscribe</span>
  </form>
  <div class="abs logo-cap"><div class="brand">eemstad<br>jeugd<br>orkest</div></div>
  <div class="abs follow">FOLLOW <i style="background:#3b5998"></i><i style="background:#1da1f2"></i><i style="background:#1b2a6b"></i></div>
  <nav class="abs main-nav">
    <a class="active" href="#">Home<svg viewBox="0 0 9 6"><path d="M1 1l3.5 3.5L8 1" fill="none" stroke="currentColor" stroke-width="1.5"/></svg></a>
    <a href="#">Orchestra<svg viewBox="0 0 9 6"><path d="M1 1l3.5 3.5L8 1" fill="none" stroke="#ec1f27" stroke-width="1.5"/></svg></a>
    <a href="#">Play along<svg viewBox="0 0 9 6"><path d="M1 1l3.5 3.5L8 1" fill="none" stroke="#ec1f27" stroke-width="1.5"/></svg></a>
    <a href="#">Concerts<svg viewBox="0 0 9 6"><path d="M1 1l3.5 3.5L8 1" fill="none" stroke="#ec1f27" stroke-width="1.5"/></svg></a>
    <a href="#">Tours<svg viewBox="0 0 9 6"><path d="M1 1l3.5 3.5L8 1" fill="none" stroke="#ec1f27" stroke-width="1.5"/></svg></a>
    <a href="#">Partners<svg viewBox="0 0 9 6"><path d="M1 1l3.5 3.5L8 1" fill="none" stroke="#ec1f27" stroke-width="1.5"/></svg></a>
    <a href="#">Friends<svg viewBox="0 0 9 6"><path d="M1 1l3.5 3.5L8 1" fill="none" stroke="#ec1f27" stroke-width="1.5"/></svg></a>
    <a href="#">Former members<svg viewBox="0 0 9 6"><path d="M1 1l3.5 3.5L8 1" fill="none" stroke="#ec1f27" stroke-width="1.5"/></svg></a>
    <a href="#">Contact us<svg viewBox="0 0 9 6"><path d="M1 1l3.5 3.5L8 1" fill="none" stroke="#ec1f27" stroke-width="1.5"/></svg></a>
  </nav>
</header>

<section class="section hero">
  <div class="abs hero-photo" role="img" aria-label="Young violinist in a light dress playing with eyes closed"></div>
  <h1 class="abs hero-title">New years concert with Lotte Verhaaren with Verbeek, Hollander and Marsh.Conductor: Ruben Aalders</h1>
  <a class="abs btn" href="#">Tickets</a>
  <div class="abs slider-arrows">
    <span><svg width="8" height="12" viewBox="0 0 8 12"><path d="M6 1L1.5 6 6 11" fill="none" stroke="#fff" stroke-width="1.8"/></svg></span>
    <span><svg width="8" height="12" viewBox="0 0 8 12"><path d="M2 1l4.5 5L2 11" fill="none" stroke="#fff" stroke-width="1.8"/></svg></span>
  </div>
</section>

<section class="section concerts">
  <div class="abs cap">Concerts</div>
  <div class="abs round-arrow" style="left:51px"><svg width="8" height="12" viewBox="0 0 8 12"><path d="M6 1L1.5 6 6 11" fill="none" stroke="#666" stroke-width="1.5"/></svg></div>
  <div class="abs round-arrow" style="left:1102px"><svg width="8" height="12" viewBox="0 0 8 12"><path d="M2 1l4.5 5L2 11" fill="none" stroke="#666" stroke-width="1.5"/></svg></div>

  <article class="abs card" style="left:130px">
    <div class="thumb" role="img" aria-label="Young violinist performing on stage"></div>
    <h3>EJO New Year's Concert</h3>
    <p>St. Anna Church,<br>Kerkplein 12, Eemstad</p>
    <div class="when">Sunday afternoon<br>January 12, 2020, 2:30 PM</div>
    <a class="btn" href="#">Book ticket</a>
  </article>
  <article class="abs card" style="left:367px">
    <div class="thumb" role="img" aria-label="Orchestra seated in a church hall"></div>
    <p style="margin-top:15px">Commemoration of 75 years of liberation Memorial Park</p>
    <p style="margin-top:4px">Memorial Park, Lindenlaan 40, Heidedorp</p>
    <div class="when">Sunday, April 19,<br>2020, 1:00 PM</div>
    <a class="btn" href="#">Book ticket</a>
  </article>
  <article class="abs card" style="left:605px">
    <div class="thumb" role="img" aria-label="Orchestra performing in front of a church altar"></div>
    <h3>EJO summer concert</h3>
    <p>St. Anna Church, Kerkplein<br>12, Eemstad</p>
    <div class="when">Saturday evening<br>11 July 2020, 20:00</div>
    <a class="btn" href="#">Book ticket</a>
  </article>
  <article class="abs card" style="left:842px">
    <div class="thumb" role="img" aria-label="Orchestra on a dimly lit stage"></div>
    <h3>Christmas concert</h3>
    <p>Hotel De Hoeve, Parkweg 8,<br>Eemstad</p>
    <div class="when">Wednesday<br>December 11, 2019</div>
    <a class="btn" href="#">Book ticket</a>
  </article>
</section>

<section class="section welcome">
  <div class="abs welcome-photo" role="img" aria-label="Young violinist with long hair holding her violin"></div>
  <div class="abs welcome-text">
    <h2>Welcome to <strong>Eemstad Jeugd Orkest</strong></h2>
    <div class="rule"></div>
    <p>The Eemstad Jeugd Orkest (EJO) is a youth orchestra that plays in a fully symphonic line-up. The orchestra has around seventy young musicians from Eemstad and the surrounding area, between the ages of thirteen and twenty-four. The musicians are mostly high school students and students. The orchestra rehearses every Friday evening in the St. Anna church in Eemstad. This rehearsal is open to the public. Whoever wants to come and listen is welcome!</p>
    <a class="btn" href="#">Read more</a>
  </div>
</section>

<section class="section ticket-sale">
  <div class="abs ticket-copy">
    <h2>Ticket sale EJO New Year's concert January 12, 2020 started!</h2>
    <p>Sed ut perspiciatis unde omnis iste natus error sit voluptatem acc usantium doloremq ue laudantium, totam rem aperiam, eaque ipsa quae ab illo inventore veritatis et quasi architecto beatae vitae dicta sunt explicabo. Nemo enim ipsam voluptatem quia voluptas sit aspe rnatur aut odit aut fugit, sed quia consequuntu.</p>
    <a class="ghost-btn" href="#">Buy tickets</a>
  </div>
  <div class="abs poster" role="img" aria-label="Colourful concert poster with programme, soloist and conductor"></div>
</section>

<section class="section upcoming">
  <div class="abs band-photo" role="img" aria-label="Young band performing on a red-lit stage"></div>
  <h2 class="abs">Upcoming <span>events</span></h2>
  <div class="abs event" style="top:126px">
    <div class="date"><small>JAN</small><b>18</b><em>2020</em></div>
    <div><h3>Maecenas facilisis mauris eget</h3><p>Aliquam vitae nibh velit. Donec faucibus, augue vitae porta bibendum, diam neque tincidunt sapien, at ornare tortor tellus sit amet magna. <b>[Read More]</b></p></div>
  </div>
  <div class="abs event" style="top:252px">
    <div class="date"><small>JAN</small><b>18</b><em>2020</em></div>
    <div><h3>Maecenas facilisis mauris eget</h3><p>Aliquam vitae nibh velit. Donec faucibus, augue vitae porta bibendum, diam neque tincidunt sapien, at ornare tortor tellus sit amet magna. <b>[Read More]</b></p></div>
  </div>
  <div class="abs event" style="top:380px">
    <div class="date"><small>JAN</small><b>18</b><em>2020</em></div>
    <div><h3>Maecenas facilisis mauris eget</h3><p>Aliquam vitae nibh velit. Donec faucibus, augue vitae porta bibendum, diam neque tincidunt sapien, at ornare tortor tellus sit amet magna. <b>[Read More]</b></p></div>
  </div>
  <a class="abs btn" href="#">Read more</a>
</section>

<section class="section recruiting">
  <div class="abs recruit-photo" role="img" aria-label="Young violinist playing on a dark stage"></div>
  <div class="abs recruit-panel"></div>
  <div class="abs recruit-copy">
    <h2>Recruiting New Musicians</h2>
    <p class="lead">NB Players are still welcome at all string groups!</p>
    <div class="rule"></div>
    <ul><li>1 Hornist</li><li>1 Bass Trombone</li><li>1 Tubaist</li><li>1 Percussionist</li></ul>
    <a class="apply" href="#">Apply now</a>
  </div>
</section>

<section class="section partners">
  <div class="abs cap">Partners</div>
  <svg class="abs chev" style="left:78px" width="14" height="24" viewBox="0 0 14 24"><path d="M12 2L2 12l10 10" fill="none" stroke="#999" stroke-width="2"/></svg>
  <svg class="abs chev" style="left:1108px" width="14" height="24" viewBox="0 0 14 24"><path d="M2 2l10 10L2 22" fill="none" stroke="#999" stroke-width="2"/></svg>
  <div class="abs partner-row">
    <span class="partner">Joris Vennema</span>
    <span class="partner"><i style="border-radius:50%"></i>Cantabile Kamerkoor</span>
    <span class="partner" style="color:#3a3a8a;font-size:15px">Mira Hofstra celliste</span>
    <span class="partner boxed">BRAM KOLK</span>
    <span class="partner" style="color:#f05a1c"><i style="background:#f05a1c"></i>Klassiek Live</span>
  </div>
</section>

<footer class="section site-footer">
  <div class="abs footer-photo" role="img" aria-label="Young violinist playing, lit dramatically against black"></div>
  <div class="abs logo-cap"><div class="brand">eemstad<br>jeugd<br>orkest</div></div>
  <ul class="abs footer-links" style="left:579px"><li>Commissies</li><li>Dirigent</li><li>Gedragscode</li><li>Orkestleden</li></ul>
  <ul class="abs footer-links" style="left:756px"><li>Auditiedata</li><li>Auditieformulier</li><li>Repetitie bezoeken</li><li>Vacatures</li></ul>
  <ul class="abs footer-links" style="left:975px"><li>Bestuur</li><li>Contact</li><li>Nieuwsbrief</li><li>Word vriend</li></ul>
  <div class="abs footer-line"></div>
  <div class="abs footer-follow">FOLLOW <i style="background:#3b5998"></i><i style="background:#1da1f2"></i><i style="background:#1b2a6b"></i></div>
  <p class="abs copyright">Copyright © 2020 All Rights Reserved</p>
</footer>

</body>
</html>
```